Brightmoor Capital Partners- Business Card

We need a professional business card that conveys confidence and trust. Strength. A modern and still yet, traditional financial planner/advisor format. I will upload a logo file or two, you do not have to use it, if it does not work for the design.

Target Market(s)

high net worth

Industry/Entity Type

Finance

Contact Information for Business Card

Address: 24853 Harlow Ave. Suite 610, Huntington Beach, CA 90318, website: brightmoorcapital.example, ph # (555) 276-1948, email address: mpellegrin@brightmoorcapital.example

```html
<!DOCTYPE html>
<html lang="en">
<head>
<meta charset="utf-8">
<title>Brightmoor Capital Partners – Business Card</title>
<link href="https://fonts.googleapis.com/css2?family=Playfair+Display:wght@400&family=Montserrat:wght@400;500;700&display=swap" rel="stylesheet">
<style>
  :root {
    --bg: #2b2e33;
    --navy: #1c2a6b;
    --navy-deep: #1a2566;
    --gold: #c9a24a;
    --ink: #2a2a2a;
    --white: #ffffff;
  }
  * { box-sizing: border-box; margin: 0; padding: 0; }
  html, body { width: 1200px; height: 900px; overflow: hidden; }
  body {
    background: var(--bg);
    display: flex;
    align-items: center;
    justify-content: center;
    gap: 40px;
    font-family: "Montserrat", sans-serif;
  }
  .card {
    width: 540px;
    height: 310px;
    border-radius: 26px;
    position: relative;
    overflow: hidden;
  }
  .card--front { background: var(--white); color: var(--ink); padding: 34px 38px; }
  .card--back { background: var(--navy-deep); }

  .brand { display: flex; align-items: center; gap: 14px; }
  .brand__mark { width: 38px; height: 38px; border-radius: 50%; border: 2px solid var(--gold); flex: none; }
  .brand__name {
    font-family: "Playfair Display", serif;
    font-size: 25px;
    letter-spacing: 1px;
    text-transform: uppercase;
    color: var(--navy);
  }

  .details { display: flex; margin-top: 34px; gap: 22px; }
  .person { width: 170px; text-align: right; padding-top: 2px; }
  .person__name { font-weight: 700; font-size: 21px; color: var(--navy); }
  .person__title { font-size: 12px; color: #555; margin-top: 2px; }
  .divider { width: 1px; background: var(--navy); height: 70px; }
  .contacts { list-style: none; font-size: 13px; display: flex; flex-direction: column; gap: 7px; }
  .contacts li { display: flex; align-items: center; gap: 10px; }
  .contacts svg { width: 13px; height: 13px; fill: var(--navy); flex: none; }

  .address { position: absolute; left: 38px; bottom: 36px; font-size: 13px; color: var(--ink); }

  .pattern { position: absolute; inset: 0; background: radial-gradient(circle at 70% 40%, #23307a, var(--navy-deep) 70%); }
  .back-brand {
    position: absolute; left: 50%; top: 60%; transform: translate(-50%, -50%);
    display: flex; align-items: center; gap: 10px;
  }
  .back-brand .brand__mark { width: 26px; height: 26px; }
  .back-brand__name {
    font-family: "Playfair Display", serif; font-size: 14px;
    letter-spacing: 1px; text-transform: uppercase; color: var(--gold);
  }
</style>
</head>
<body>
  <article class="card card--front">
    <header class="brand">
      <span class="brand__mark"></span>
      <h1 class="brand__name">Brightmoor Capital Partners</h1>
    </header>
    <section class="details">
      <div class="person">
        <p class="person__name">Daniel Ashford</p>
        <p class="person__title">Managing Director</p>
      </div>
      <span class="divider"></span>
      <ul class="contacts">
        <li>
          <svg viewBox="0 0 24 24"><path d="M6.6 10.8a15.1 15.1 0 0 0 6.6 6.6l2.2-2.2a1 1 0 0 1 1-.25 11.4 11.4 0 0 0 3.6.57 1 1 0 0 1 1 1V20a1 1 0 0 1-1 1A17 17 0 0 1 3 4a1 1 0 0 1 1-1h3.5a1 1 0 0 1 1 1c0 1.25.2 2.45.57 3.57a1 1 0 0 1-.25 1z"/></svg>
          555-276-1948
        </li>
        <li>
          <svg viewBox="0 0 24 24"><path d="M2 5h20v14H2z M2 5l10 8 10-8" /></svg>
          info@brightmoorcapital.example
        </li>
        <li>
          <svg viewBox="0 0 24 24"><circle cx="12" cy="12" r="10"/></svg>
          www.brightmoorcapital.example
        </li>
      </ul>
    </section>
    <p class="address">24853 Harlow Ave. Suite 610 Huntington Beach, CA 90318</p>
  </article>

  <article class="card card--back">
    <div class="pattern" role="img" aria-label="Tone-on-tone navy pattern of repeating brand emblems"></div>
    <div class="back-brand">
      <span class="brand__mark"></span>
      <span class="back-brand__name">Brightmoor Capital Partners</span>
    </div>
  </article>
</body>
</html>
```